I need a flyer made , the flyer can be one page or two pages or three pages . I will be posting this on Instagram and social media platforms. I am a luxury home builder , I am looking to hire a construction project manager . Below are some examples and ideas what can be on the flyer

We’re looking for a construction project manager who’s passionate about building luxury homes at the highest standards
We’re hiring construction project manager
* Experience 5+ years in residential project management with a strong portfolio of completed homes.
* location : Bergen County NJ
* excellent leadership skills, leads teams with confidence and clarity
* communicates seamlessly with architects , engineers, designers and clients
*knows how to manage budgets and timelines without compromising quality
*solves problems with a positive solution first mindset
* pays attention to every detail because in luxury the small things are the big things

Apply now , link in bio or DM to connect.

My logo is attached, my web site www.ridgelanebuilders.com
My style is modern but still warm and inviting. I like a clean classy look .
Updates

Please don’t add any images of chairs or people to the flyer , I do not want people on my flyer. Do not add standard images of offices and houses , we are luxury builders , we build homes over 2 million dollars. Keep a classy , simple modern look . High end .

You can add a white hard hat with my logo on it for a image , this is a suggestion does not have to be on my flyer ,

```html
<!DOCTYPE html>
<html lang="en">
<head>
<meta charset="utf-8">
<title>Ridgelane Builders – Hiring Construction Project Manager</title>
<link rel="stylesheet" href="https://fonts.googleapis.com/css2?family=Poppins:wght@300;400;500;600;700;800;900&family=Great+Vibes&display=swap">
<style>
  :root {
    --backdrop: #666666;
    --paper: #f7f7f7;
    --ink: #000000;
    --charcoal: #2a2a2a;
    --slate: #4a4a4a;
    --white: #ffffff;
    --pin-red: #e31b1b;
    --pin-light: #f26a6a;
    --pin-dark: #b80f0f;
    --sketch: #d9d9d9;
    --tick: #dddddd;
    --outline: #9a9a9a;
  }
  * { box-sizing: border-box; margin: 0; padding: 0; }
  html, body {
    width: 1045px; height: 1200px; overflow: hidden;
    background: var(--backdrop);
    font-family: "Poppins", sans-serif;
    color: var(--ink);
  }
  .flyer {
    position: absolute; left: 79px; top: 156px;
    width: 888px; height: 888px; overflow: hidden;
    background:
      linear-gradient(160deg, rgba(255,255,255,0) 30%, rgba(225,225,225,.55) 45%, rgba(255,255,255,0) 60%),
      linear-gradient(200deg, rgba(255,255,255,.9) 10%, rgba(230,230,230,.6) 70%, rgba(250,250,250,.9) 100%),
      var(--paper);
  }
  .sketch-area {
    position: absolute; left: 0; top: 19px; width: 446px; height: 460px;
    background: radial-gradient(ellipse at 30% 55%, var(--sketch) 0%, rgba(217,217,217,.45) 45%, rgba(247,247,247,0) 75%);
  }
  .pin { position: absolute; left: 127px; top: 190px; width: 153px; height: 235px; }
  .pin-label {
    position: absolute; left: 140px; top: 244px; width: 153px;
    text-align: center; font-weight: 700; font-size: 16.5px; line-height: 17.5px;
  }
  .script {
    position: absolute; left: 305px; top: 62px;
    font-family: "Great Vibes", cursive; font-size: 118px; line-height: 1;
  }
  .headline {
    position: absolute; left: 306px; top: 168px;
    font-weight: 900; font-size: 130px; line-height: 1; letter-spacing: -3px;
  }
  .role-line-1 {
    position: absolute; left: 308px; top: 301px;
    font-weight: 800; font-size: 40px; line-height: 1; letter-spacing: -1.2px;
  }
  .role-line-2 {
    position: absolute; left: 308px; top: 344px;
    font-size: 34px; line-height: 1; letter-spacing: -1px;
  }
  .role-line-2 .light { font-weight: 300; }
  .role-line-2 .bold { font-weight: 800; }
  .tagline {
    position: absolute; left: 308px; top: 393px; height: 38px; display: flex;
  }
  .tagline span {
    display: flex; align-items: center; justify-content: center;
    color: var(--white); font-size: 15.5px; font-weight: 400; height: 38px;
  }
  .tagline b { font-weight: 800; margin-left: 4px; }
  .tag-build { background: var(--ink); width: 158px; border-radius: 19px 0 0 19px; }
  .tag-lead { background: var(--slate); width: 159px; border-radius: 0 19px 19px 0; margin-left: 2px; }
  .requirements {
    position: absolute; left: 55px; top: 483px; width: 778px; height: 215px;
    border-radius: 28px; overflow: hidden; display: flex; color: var(--white);
  }
  .req-col { list-style: none; padding: 30px 0 0 34px; font-size: 15.5px; line-height: 17.8px; }
  .req-col.left { background: var(--ink); width: 388px; padding-right: 44px; }
  .req-col.right { background: var(--charcoal); flex: 1; padding-left: 18px; padding-right: 52px; }
  .req-col li { position: relative; padding-left: 18px; margin-bottom: 12px; font-weight: 400; }
  .req-col li b { font-weight: 700; }
  .req-col li svg { position: absolute; left: 0; top: 4px; width: 11px; height: 11px; }
  .brand {
    position: absolute; left: 46px; top: 750px; width: 246px; text-align: center;
    font-weight: 500; line-height: 1;
  }
  .brand-main { font-size: 40px; letter-spacing: 2px; display: block; }
  .brand-sub { font-size: 20px; letter-spacing: 5px; display: block; margin-top: 10px; }
  .cta { position: absolute; left: 320px; top: 745px; height: 38px; display: flex; }
  .cta-apply {
    width: 152px; height: 38px; border-radius: 19px; background: var(--ink); color: var(--white);
    font-weight: 700; font-size: 18.5px; display: flex; align-items: center; justify-content: center;
    position: relative; z-index: 1;
  }
  .cta-link {
    width: 308px; height: 38px; border-radius: 19px; border: 1px solid var(--outline); background: var(--white);
    font-weight: 700; font-size: 17.5px; display: flex; align-items: center; justify-content: center;
    margin-left: -3px; padding-left: 6px;
  }
  .contact-head { position: absolute; top: 793px; font-weight: 700; font-size: 16.5px; line-height: 20px; }
  .follow-head { left: 320px; }
  .visit-head { left: 617px; }
  .handles { position: absolute; top: 814px; height: 20px; font-size: 13.5px; line-height: 20px; display: flex; align-items: center; white-space: nowrap; }
  .handles.social { left: 319px; width: 282px; }
  .handles.web { left: 617px; font-size: 14.5px; }
  .handle { display: flex; align-items: center; margin-right: 10px; }
  .handle:last-child { margin-right: 0; }
  .handle i {
    display: inline-block; width: 11px; height: 11px; border-radius: 50%;
    background: var(--ink); margin-right: 5px; flex: none;
  }
  .divider { position: absolute; left: 608px; top: 796px; width: 1px; height: 37px; background: var(--ink); }
</style>
</head>
<body>
  <main class="flyer">
    <div class="sketch-area" role="img" aria-label="Faint architectural line sketch of a modern multi-level building"></div>

    <svg class="pin" viewBox="0 0 153 235" aria-hidden="true">
      <defs>
        <linearGradient id="pinFill" x1="0" y1="0" x2="1" y2="1">
          <stop offset="0" stop-color="var(--pin-light)"/>
          <stop offset=".45" stop-color="var(--pin-red)"/>
          <stop offset="1" stop-color="var(--pin-dark)"/>
        </linearGradient>
      </defs>
      <path d="M76.5 2C36 2 2 34 2 76c0 46 58 124 74.5 157C93 200 151 122 151 76 151 34 117 2 76.5 2Z" fill="url(#pinFill)"/>
      <circle cx="90" cy="78" r="42" fill="var(--white)"/>
    </svg>
    <p class="pin-label">Bergen<br>County,<br>NJ</p>

    <p class="script">We're</p>
    <h1 class="headline">HIRING</h1>
    <p class="role-line-1">CONSTRUCTION</p>
    <p class="role-line-2"><span class="light">PROJECT</span> <span class="bold">MANAGER</span></p>

    <div class="tagline">
      <span class="tag-build">BUILD<b>LUXURY</b></span>
      <span class="tag-lead">LEAD<b>EXCELLENCE</b></span>
    </div>

    <section class="requirements">
      <ul class="req-col left">
        <li><svg viewBox="0 0 12 12"><circle cx="6" cy="6" r="6" fill="var(--tick)"/><path d="M3.2 6.2l1.9 1.8 3.7-3.9" stroke="var(--ink)" stroke-width="1.5" fill="none"/></svg>Experience <b>5+ years</b> in residential project management with a strong portfolio of completed homes.</li>
        <li><svg viewBox="0 0 12 12"><circle cx="6" cy="6" r="6" fill="var(--tick)"/><path d="M3.2 6.2l1.9 1.8 3.7-3.9" stroke="var(--ink)" stroke-width="1.5" fill="none"/></svg>Excellent <b>leadership skills</b>, leads teams with confidence and clarity</li>
        <li><svg viewBox="0 0 12 12"><circle cx="6" cy="6" r="6" fill="var(--tick)"/><path d="M3.2 6.2l1.9 1.8 3.7-3.9" stroke="var(--ink)" stroke-width="1.5" fill="none"/></svg><b>Communicates seamlessly</b> with architects , engineers, designers and clients</li>
      </ul>
      <ul class="req-col right">
        <li><svg viewBox="0 0 12 12"><circle cx="6" cy="6" r="6" fill="var(--tick)"/><path d="M3.2 6.2l1.9 1.8 3.7-3.9" stroke="var(--charcoal)" stroke-width="1.5" fill="none"/></svg>Knows how to <b>manage budgets and timelines</b> without compromising quality</li>
        <li><svg viewBox="0 0 12 12"><circle cx="6" cy="6" r="6" fill="var(--tick)"/><path d="M3.2 6.2l1.9 1.8 3.7-3.9" stroke="var(--charcoal)" stroke-width="1.5" fill="none"/></svg><b>Solves problems</b> with a positive solution first mindset</li>
        <li><svg viewBox="0 0 12 12"><circle cx="6" cy="6" r="6" fill="var(--tick)"/><path d="M3.2 6.2l1.9 1.8 3.7-3.9" stroke="var(--charcoal)" stroke-width="1.5" fill="none"/></svg><b>Pays attention to every detail</b> because in luxury the small things are the big things</li>
      </ul>
    </section>

    <div class="brand">
      <span class="brand-main">RIDGELANE</span>
      <span class="brand-sub">builders</span>
    </div>

    <div class="cta">
      <span class="cta-apply">Apply now</span>
      <span class="cta-link">Link in bio or DM to connect</span>
    </div>

    <p class="contact-head follow-head">Follow us</p>
    <p class="contact-head visit-head">Visit us</p>
    <div class="handles social">
      <span class="handle"><i></i>ridgelanebuilders</span>
      <span class="handle"><i></i>RidgelaneHomes</span>
    </div>
    <div class="divider"></div>
    <div class="handles web">www.ridgelanebuilders.com</div>
  </main>
</body>
</html>
```